iOS App Design - Google Material Design + Nimbus

What we would love to do is to create an activity feed page plus main navigation for our iOS application. If we like this design then we'd like to hire someone to take the design elements and build out the rest of our screens.

The design must use Google Material Design and be delivered in a Nimbus file.

Our product is an application for activity provider owners to manage their daily business while on the go. This activity feed/home screen will provide them with information about their bookings, tours that day, etc.

We would like for it to be modern and eye catching, yet simple and functional for someone to use outdoors and while not in an office.

For this home screen, the main elements we would like to include:

- Main App Navigation with 4 elements: Home, Availability/Calendar, Booking and Settings
- A way to add a booking (plus sign or similar that is a constant - nav or floating

- A couple of overall key metrics that indicate how you the user’s business is doing that month that are static - not part of the feed

- A way to show different types of activity in a "news feed" - i.e. if a booking has happened or there is an upcoming tour, if a payment has been made to your account, suggestion on how to improve your profile.

- A way to filter the activities

We are open to the layout and options for these main elements above, we would like your opinion on how best from a user design perspective we can implement these.

Please let us know if you have any questions.

```html
<!DOCTYPE html>
<html lang="en">
<head>
<meta charset="utf-8">
<title>Your Bookings – Home</title>
<link rel="stylesheet" href="https://fonts.googleapis.com/css2?family=Roboto:wght@300;400;500;700&display=swap">
<style>
  :root {
    --canvas-bg: #e6e6e3;
    --blue-dark: #1c7fc9;
    --blue: #2794db;
    --blue-light: #46aeea;
    --surface: #ffffff;
    --feed-bg: #eef0f2;
    --text: #1d1f22;
    --text-muted: #8a9097;
    --line: #d9dde1;
    --alert: #f0502f;
  }
  * { box-sizing: border-box; margin: 0; padding: 0; }
  html, body { width: 1200px; height: 893px; overflow: hidden; }
  body {
    background: var(--canvas-bg);
    font-family: "Roboto", sans-serif;
    color: var(--text);
    position: relative;
  }
  .app-screen {
    position: absolute;
    left: 390px; top: 73px;
    width: 420px; height: 747px;
    background: var(--feed-bg);
    overflow: hidden;
    box-shadow: 0 6px 30px rgba(0,0,0,.12);
  }
  /* Header */
  .app-header {
    height: 124px;
    background: linear-gradient(100deg, var(--blue-dark), var(--blue-light));
    color: #fff;
    padding: 0 16px;
  }
  .status-bar {
    height: 24px;
    display: flex; align-items: center; justify-content: space-between;
    font-size: 12px; font-weight: 500;
  }
  .status-bar .carrier { display: flex; align-items: center; gap: 5px; }
  .status-bar .battery { display: flex; align-items: center; gap: 5px; }
  .app-title { font-size: 20px; font-weight: 500; margin-top: 10px; }
  .tab-bar {
    display: flex; align-items: flex-end; justify-content: space-between;
    margin-top: 16px; font-size: 13px; font-weight: 500; letter-spacing: .5px;
  }
  .tab { padding: 0 18px 12px; opacity: .8; }
  .tab.is-active { opacity: 1; border-bottom: 3px solid #fff; padding-bottom: 9px; }
  .tab-search { padding-bottom: 10px; }

  /* Metrics */
  .metrics {
    display: flex; gap: 8px; padding: 8px 8px 0;
  }
  .metric-card {
    flex: 1; height: 150px; background: var(--surface);
    border-radius: 3px; box-shadow: 0 1px 3px rgba(0,0,0,.1);
    display: flex; flex-direction: column; align-items: center; justify-content: center;
    position: relative;
  }
  .ring-value {
    position: absolute; top: 50%; left: 50%; transform: translate(-50%,-50%);
    text-align: center;
  }
  .ring-value strong { display: block; font-size: 26px; font-weight: 500; }
  .ring-value span { display: block; font-size: 11px; color: #444; line-height: 1.2; }
  .bar-caption { font-size: 12px; color: #333; margin-top: 6px; }

  /* Feed filter */
  .feed-filter {
    text-align: center; font-size: 12px; font-weight: 500; letter-spacing: 1px;
    color: #444; padding: 16px 0 10px; margin-left: 60px;
  }

  /* Feed timeline */
  .feed { position: relative; padding: 0 8px 0 72px; }
  .feed::before {
    content: ""; position: absolute; left: 36px; top: -20px; bottom: -200px;
    width: 2px; background: var(--blue);
  }
  .feed-item { position: relative; margin-bottom: 10px; }
  .feed-icon {
    position: absolute; left: -54px; top: 6px;
    width: 38px; height: 38px; border-radius: 50%;
    background: var(--blue); display: flex; align-items: center; justify-content: center;
    box-shadow: 0 0 0 4px var(--feed-bg);
  }
  .feed-card {
    background: var(--surface); border-radius: 3px;
    box-shadow: 0 1px 3px rgba(0,0,0,.1);
    padding: 10px 14px; min-height: 74px;
  }
  .feed-kicker { font-size: 9px; letter-spacing: 1px; color: var(--text-muted); font-weight: 500; }
  .feed-title { font-size: 15px; font-weight: 500; margin: 3px 0 5px; }
  .feed-meta { display: flex; gap: 14px; font-size: 11px; color: #555; }
  .feed-meta span { display: flex; align-items: center; gap: 4px; }
  .feed-card.is-stub { min-height: 40px; }

  /* FAB */
  .fab-add {
    position: absolute; right: 22px; bottom: 74px;
    width: 48px; height: 48px; border-radius: 50%;
    background: var(--blue);
    box-shadow: 0 3px 8px rgba(0,0,0,.25);
    display: flex; align-items: center; justify-content: center;
  }

  /* Bottom nav */
  .bottom-nav {
    position: absolute; left: 0; right: 0; bottom: 0; height: 58px;
    background: var(--surface); border-top: 1px solid var(--line);
    display: flex;
  }
  .nav-item {
    flex: 1; display: flex; flex-direction: column; align-items: center; justify-content: center;
    gap: 3px; font-size: 10px; color: var(--text-muted); position: relative;
  }
  .nav-item.is-active { color: var(--blue); }
  .nav-badge {
    position: absolute; top: 12px; left: 56%;
    width: 7px; height: 7px; border-radius: 50%; background: var(--alert);
  }
</style>
</head>
<body>
<main class="app-screen">
  <header class="app-header">
    <div class="status-bar">
      <span class="carrier">
        <svg width="18" height="10" viewBox="0 0 18 10" fill="#fff"><rect x="0" y="6" width="3" height="4"/><rect x="5" y="4" width="3" height="6"/><rect x="10" y="2" width="3" height="8"/><rect x="15" y="0" width="3" height="10"/></svg>
        Nimbus
        <svg width="14" height="10" viewBox="0 0 14 10" fill="none" stroke="#fff" stroke-width="1.6"><path d="M1 3.5a9 9 0 0 1 12 0M3.5 6a5.5 5.5 0 0 1 7 0"/><circle cx="7" cy="8.6" r="1" fill="#fff"/></svg>
      </span>
      <span class="clock">9:41 AM</span>
      <span class="battery">100%
        <svg width="24" height="11" viewBox="0 0 24 11"><rect x=".5" y=".5" width="20" height="10" rx="2" fill="none" stroke="#fff"/><rect x="2" y="2" width="17" height="7" rx="1" fill="#fff"/><rect x="21.5" y="3.5" width="2" height="4" rx="1" fill="#fff"/></svg>
      </span>
    </div>
    <h1 class="app-title">Your Bookings</h1>
    <nav class="tab-bar">
      <span class="tab is-active">NEW</span>
      <span class="tab">UPCOMING</span>
      <span class="tab">PAST</span>
      <span class="tab-search">
        <svg width="18" height="18" viewBox="0 0 18 18" fill="none" stroke="#fff" stroke-width="2"><circle cx="7.5" cy="7.5" r="5.5"/><path d="M11.5 11.5L16 16"/></svg>
      </span>
    </nav>
  </header>

  <section class="metrics">
    <div class="metric-card metric-completed">
      <svg width="112" height="112" viewBox="0 0 112 112">
        <circle cx="56" cy="56" r="46" fill="none" stroke="#e4eef6" stroke-width="8"/>
        <circle cx="56" cy="56" r="46" fill="none" stroke="var(--blue)" stroke-width="8"
                stroke-dasharray="192.7 289" transform="rotate(-90 56 56)" stroke-linecap="round"/>
      </svg>
      <div class="ring-value"><strong>8/12</strong><span>Bookings<br>completed</span></div>
    </div>
    <div class="metric-card metric-trend">
      <svg width="150" height="92" viewBox="0 0 150 92" fill="var(--blue)">
        <rect x="4" y="52" width="9" height="40" rx="3"/>
        <rect x="20" y="36" width="9" height="56" rx="3"/>
        <rect x="36" y="22" width="9" height="70" rx="3"/>
        <rect x="52" y="30" width="9" height="62" rx="3"/>
        <rect x="68" y="14" width="9" height="78" rx="3"/>
        <rect x="84" y="34" width="9" height="58" rx="3"/>
        <rect x="100" y="4" width="9" height="88" rx="3"/>
        <rect x="116" y="26" width="9" height="66" rx="3"/>
        <rect x="132" y="44" width="9" height="48" rx="3"/>
      </svg>
      <p class="bar-caption">Bookings up 31% this week</p>
    </div>
  </section>

  <div class="feed-filter">UPCOMING &#8964;</div>

  <section class="feed">
    <article class="feed-item">
      <div class="feed-icon">
        <svg width="18" height="18" viewBox="0 0 18 18" fill="none" stroke="#fff" stroke-width="1.6"><rect x="3" y="2" width="12" height="14" rx="1.5"/><path d="M6 6h6M6 9h6M6 12h4"/></svg>
      </div>
      <div class="feed-card">
        <p class="feed-kicker">UPCOMING BOOKING</p>
        <h2 class="feed-title">Booking with Dana Reyes</h2>
        <div class="feed-meta">
          <span><svg width="11" height="11" viewBox="0 0 12 12" fill="none" stroke="#555" stroke-width="1.2"><circle cx="6" cy="6" r="5"/><path d="M6 3v3l2 1"/></svg>13.30pm</span>
          <span><svg width="10" height="12" viewBox="0 0 10 12" fill="none" stroke="#555" stroke-width="1.2"><path d="M5 11S1 7 1 4.5a4 4 0 0 1 8 0C9 7 5 11 5 11z"/><circle cx="5" cy="4.5" r="1.3"/></svg>Larkford</span>
        </div>
      </div>
    </article>
    <article class="feed-item">
      <div class="feed-icon">
        <svg width="16" height="18" viewBox="0 0 16 18" fill="none" stroke="#fff" stroke-width="1.6"><path d="M8 16S2 10.5 2 6.5a6 6 0 0 1 12 0C14 10.5 8 16 8 16z"/><circle cx="8" cy="6.5" r="2"/></svg>
      </div>
      <div class="feed-card">
        <p class="feed-kicker">UPCOMING TOUR</p>
        <h2 class="feed-title">Tour with Dana Reyes</h2>
        <div class="feed-meta">
          <span><svg width="11" height="11" viewBox="0 0 12 12" fill="none" stroke="#555" stroke-width="1.2"><circle cx="6" cy="6" r="5"/><path d="M6 3v3l2 1"/></svg>13.30pm</span>
          <span><svg width="10" height="12" viewBox="0 0 10 12" fill="none" stroke="#555" stroke-width="1.2"><path d="M5 11S1 7 1 4.5a4 4 0 0 1 8 0C9 7 5 11 5 11z"/><circle cx="5" cy="4.5" r="1.3"/></svg>Larkford</span>
        </div>
      </div>
    </article>
    <article class="feed-item">
      <div class="feed-icon">
        <svg width="18" height="16" viewBox="0 0 18 16" fill="none" stroke="#fff" stroke-width="1.6"><ellipse cx="9" cy="8.5" rx="6.5" ry="5"/><path d="M5 13v2M13 13v2M9 3.5V2"/><circle cx="12" cy="7" r=".6" fill="#fff"/></svg>
      </div>
      <div class="feed-card">
        <p class="feed-kicker">PAYMENT RECEIVED</p>
        <h2 class="feed-title">$45.50 received from Dana Reyes</h2>
      </div>
    </article>
    <article class="feed-item">
      <div class="feed-card is-stub"></div>
    </article>
  </section>

  <div class="fab-add" aria-label="Add booking">
    <svg width="18" height="18" viewBox="0 0 18 18" stroke="#fff" stroke-width="2.4" stroke-linecap="round"><path d="M9 3v12M3 9h12"/></svg>
  </div>

  <nav class="bottom-nav">
    <div class="nav-item is-active">
      <svg width="20" height="18" viewBox="0 0 20 18" fill="none" stroke="currentColor" stroke-width="1.6"><path d="M2 8.5L10 2l8 6.5M4.5 7v9h11V7"/><path d="M8 16v-5h4v5"/></svg>
      Home
    </div>
    <div class="nav-item">
      <svg width="18" height="18" viewBox="0 0 18 18" fill="none" stroke="currentColor" stroke-width="1.6"><rect x="2" y="3" width="14" height="13" rx="1.5"/><path d="M2 7h14M6 1.5v3M12 1.5v3"/></svg>
      Calendar
    </div>
    <div class="nav-item">
      <svg width="18" height="18" viewBox="0 0 18 18" fill="none" stroke="currentColor" stroke-width="1.6"><path d="M3 9l6-6h6v6l-6 6z"/><circle cx="12" cy="6" r="1"/></svg>
      Bookings
    </div>
    <div class="nav-item">
      <svg width="18" height="18" viewBox="0 0 18 18" fill="none" stroke="currentColor" stroke-width="1.6"><circle cx="9" cy="9" r="2.5"/><path d="M9 1.5v2.5M9 14v2.5M1.5 9H4M14 9h2.5M3.7 3.7l1.8 1.8M12.5 12.5l1.8 1.8M3.7 14.3l1.8-1.8M12.5 5.5l1.8-1.8"/></svg>
      Settings
      <span class="nav-badge"></span>
    </div>
  </nav>
</main>
</body>
</html>
```